Tarrow Vitamins Sign

I need to make a sign that looks like a vintage metal sign like you would find in an old pharmacy. I'm attaching a few examples of the look and feel. The text is attached in the word file

```html
<!DOCTYPE html>
<html lang="en">
<head>
<meta charset="utf-8">
<title>Tarrow Vitamins Sign</title>
<link rel="stylesheet" href="https://fonts.googleapis.com/css2?family=Rye&display=swap">
<style>
  :root {
    --frame-teal: #7fa9a4;
    --panel-teal: #22424a;
    --ornament-tone: #2b4e55;
    --cream: #f3f8f2;
    --brick-red: #b9503f;
    --soft-teal: #7ba8a3;
  }
  html, body {
    margin: 0;
    padding: 0;
    width: 1200px;
    height: 1002px;
    overflow: hidden;
    background: var(--frame-teal);
  }
  .sign {
    position: relative;
    width: 1200px;
    height: 1002px;
    background: var(--frame-teal);
  }
  .sign__panel {
    position: absolute;
    left: 16px;
    top: 13px;
    width: 1168px;
    height: 976px;
    background: var(--panel-teal);
  }
  .sign__ornament {
    position: absolute;
    width: 300px;
    height: 340px;
    background: var(--ornament-tone);
    opacity: 0.55;
  }
  .sign__ornament--tl { left: 48px; top: 30px; border-radius: 0 0 160px 0; }
  .sign__ornament--tr { right: 48px; top: 30px; border-radius: 0 0 0 160px; }
  .sign__ornament--bl { left: 48px; bottom: 30px; border-radius: 0 160px 0 0; }
  .sign__ornament--br { right: 48px; bottom: 30px; border-radius: 160px 0 0 0; }
  .sign__type {
    position: absolute;
    inset: 0;
    font-family: "Rye", serif;
  }
  .tagline {
    fill: var(--soft-teal);
    stroke: var(--panel-teal);
    stroke-width: 1.5px;
    paint-order: stroke;
  }
  .brand-shadow {
    fill: var(--brick-red);
  }
  .brand {
    fill: var(--cream);
    stroke: var(--brick-red);
    stroke-width: 6px;
    paint-order: stroke;
  }
</style>
</head>
<body>
  <main class="sign">
    <div class="sign__panel"></div>
    <div class="sign__ornament sign__ornament--tl" role="img" aria-label="Engraved leafy scroll ornament, top left corner"></div>
    <div class="sign__ornament sign__ornament--tr" role="img" aria-label="Engraved leafy scroll ornament, top right corner"></div>
    <div class="sign__ornament sign__ornament--bl" role="img" aria-label="Engraved leafy scroll ornament, bottom left corner"></div>
    <div class="sign__ornament sign__ornament--br" role="img" aria-label="Engraved leafy scroll ornament, bottom right corner"></div>

    <svg class="sign__type" width="1200" height="1002" viewBox="0 0 1200 1002" aria-label="Tarrow Vitamins, since 70,000 BCE, history of humankind">
      <text class="tagline" transform="translate(395 252) rotate(-18)" text-anchor="middle" font-size="52" textLength="500" lengthAdjust="spacingAndGlyphs">Since 70,000 BCE</text>

      <g transform="translate(625 455) rotate(-18)">
        <text class="brand-shadow" x="-8" y="10" text-anchor="middle" font-size="190" textLength="420" lengthAdjust="spacingAndGlyphs">Tarrow</text>
        <text class="brand" x="0" y="0" text-anchor="middle" font-size="190" textLength="420" lengthAdjust="spacingAndGlyphs">Tarrow</text>
      </g>

      <g transform="translate(610 690) rotate(-18)">
        <text class="brand-shadow" x="-8" y="10" text-anchor="middle" font-size="190" textLength="820" lengthAdjust="spacingAndGlyphs">Vitamins</text>
        <text class="brand" x="0" y="0" text-anchor="middle" font-size="190" textLength="820" lengthAdjust="spacingAndGlyphs">Vitamins</text>
      </g>

      <text class="tagline" transform="translate(772 772) rotate(-18)" text-anchor="middle" font-size="50" textLength="570" lengthAdjust="spacingAndGlyphs">history of humankind</text>
    </svg>
  </main>
</body>
</html>
```